Steelcrest Process Systems. Needs a Business Card Design

We need a business card design for an engineering company which supplies industrial components (pumps, compressors, mechanical seals) provides repairs and services for above mentioned equipments. We offer a uniqe engineering solutions which help our customers to increase the productivness of their manufacturings, and energy savings.

Target Market(s)

Chemical and energy plants, refineries. Food industry and private consumers in a less.

Industry/Entity Type

Business

Contact Information for Business Card

Stylish and sleek design oriented on industrial area.

Requirements
Should not have
• company name shortening

```html
<!DOCTYPE html>
<html lang="en">
<head>
<meta charset="UTF-8">
<title>Steelcrest Process Systems – Business Cards</title>
<link href="https://fonts.googleapis.com/css2?family=Baloo+2:wght@600&family=Fjalla+One&family=Roboto:wght@400&display=swap" rel="stylesheet">
<style>
  :root {
    --backdrop: #d9d8d8;
    --card: #ffffff;
    --navy: #1b4594;
    --blue: #1d479b;
    --red: #e1322b;
    --amber: #f2a922;
    --rule: #d6d9df;
  }
  * { margin: 0; padding: 0; box-sizing: border-box; }
  html, body { width: 1200px; height: 1200px; overflow: hidden; }
  body { background: var(--backdrop); position: relative; font-family: "Roboto", Arial, sans-serif; }

  .card {
    position: absolute;
    background: var(--card);
    width: 712px;
    height: 418px;
    overflow: hidden;
  }
  .card--front { left: 238px; top: 119px; }
  .card--back { left: 231px; top: 645px; }

  .brand-name {
    font-family: "Baloo 2", "Trebuchet MS", sans-serif;
    font-weight: 600;
    color: var(--navy);
  }
  .brand-dot {
    border-radius: 50%;
    background: var(--red);
  }

  /* front */
  .front-brand {
    position: absolute;
    left: 0; right: 0; top: 112px;
    display: flex; flex-direction: column; align-items: center;
  }
  .front-brand .brand-dot { width: 96px; height: 96px; }
  .front-brand .brand-name { font-size: 36px; line-height: 1; margin-top: 66px; letter-spacing: 0.2px; }

  /* back */
  .back-brand {
    position: absolute; left: 40px; top: 56px;
    display: flex; align-items: center;
  }
  .back-brand .brand-dot { width: 96px; height: 96px; margin-right: 44px; }
  .back-brand .divider { width: 1px; height: 122px; background: var(--rule); margin-right: 22px; }
  .back-brand .brand-name { font-size: 44px; line-height: 46px; }

  .person { position: absolute; left: 46px; top: 234px; }
  .person-name {
    font-family: "Fjalla One", "Arial Narrow", sans-serif;
    font-size: 26px; color: var(--navy); line-height: 1.1;
  }
  .person-role { font-size: 16px; color: var(--navy); margin-top: 6px; }

  .contact { position: absolute; left: 368px; top: 236px; color: var(--navy); font-size: 17.5px; }
  .contact-row { display: flex; align-items: center; height: 25px; }
  .contact-row svg { width: 18px; height: 14px; margin-right: 17px; fill: var(--red); }
  .accent { color: var(--red); }
  .address { margin-top: 10px; line-height: 23px; }

  .footer-band { position: absolute; left: 0; bottom: 0; width: 712px; height: 18px; }
</style>
</head>
<body>
  <section class="card card--front">
    <div class="front-brand">
      <span class="brand-dot"></span>
      <span class="brand-name">Steelcrest Process Systems</span>
    </div>
  </section>

  <section class="card card--back">
    <div class="back-brand">
      <span class="brand-dot"></span>
      <span class="divider"></span>
      <span class="brand-name">Steelcrest<br>Process Systems</span>
    </div>

    <div class="person">
      <div class="person-name">Your Good Name</div>
      <div class="person-role">Managing Director</div>
    </div>

    <div class="contact">
      <div class="contact-row">
        <svg viewBox="0 0 18 14" aria-hidden="true"><path d="M1 5c0-3 4-4 8-4s8 1 8 4l-3 1-1-2H5L4 6 1 5zM4 7h10l1 6H3z"/></svg>
        <span>+00 111 222 3333</span>
      </div>
      <div class="contact-row">
        <svg viewBox="0 0 18 14" aria-hidden="true"><circle cx="9" cy="7" r="6.5"/><path d="M2.5 7h13M9 .5v13M4 3.5h10M4 10.5h10" stroke="#fff" stroke-width="1" fill="none"/></svg>
        <span>www.<span class="accent">yourwebsite</span>.com</span>
      </div>
      <div class="contact-row">
        <svg viewBox="0 0 18 14" aria-hidden="true"><rect x="1" y="2" width="16" height="11"/><path d="M1 2l8 6 8-6" stroke="#fff" stroke-width="1.3" fill="none"/></svg>
        <span>yourname@yourwebsite.com</span>
      </div>
      <div class="address">Your Long Commercial or<br>business address in 2 line</div>
    </div>

    <svg class="footer-band" viewBox="0 0 712 18" preserveAspectRatio="none" aria-hidden="true">
      <polygon points="0,0 500,0 470,18 0,18" fill="var(--red)"/>
      <polygon points="505,0 712,0 712,18 470,18" fill="var(--blue)"/>
    </svg>
  </section>
</body>
</html>
```